Stationary, business cards, referral form
Corvale Dental Partners
Professional
Center for Endodontics, Periodontics and Implant Dentistry
4820 Quillby Road NE
Suite 67
Harlow Falls, ND 58990
info@corvaledentalpartners.example
www.corvaledentalpartners.example
I need a business card for 3 different doctors.
Brenna K. Solvik, DDS
General and Cosmetic Dentistry
Peter Ostrand, DDS
Endodontics
Daniel Frayce, DDS
Periodontics and Implant Dentistry
Also I need a business card that is just a generic CORVALE DENTAL PARTNERS and it would have all the doctors listed on it.
I also need:
Letterhead, envelopes (stationary)
Folder
Patient Referral Forms
Patient 2 types of referral form: (see the document attached)
1. Periodontics Referral form. On top it would have Daniel Frayce, DDS and our office info
Date:
Patient Name:
Evaluation of: Please use the same options as in the example in attached doc
Radiographs: use three options from the example doc.
Referring Doctor: Name, phone address, signature
The other referral form in same format as the periodontics one except on top it says
Office Information
Also under EVALUATION OF it gives options for:
* Root Canal Therapy
* Root Canal Retreatment
* Apicoectomy
* Other
Again please see the example of what referral document attached.
Please message me with questions
Appointment Information.
Space for Date, Time, etc.
Cancellation policy.
We kindly ask for a 24hr notice for cancellation of appointments otherwise a charge may be incurred.

```html
<!DOCTYPE html>
<html lang="en">
<head>
<meta charset="utf-8">
<title>Corvale Dental Partners — Stationery Set</title>
<link rel="stylesheet" href="https://fonts.googleapis.com/css2?family=Cormorant+Garamond:wght@500;600&family=Open+Sans:wght@400;600&display=swap">
<style>
:root{
  --bg:#f3f4f6;
  --paper:#ffffff;
  --navy:#0e2c5e;
  --blue:#1f56a3;
  --sky:#4f86cf;
  --mist:#e6edf7;
  --grey:#9aa3ad;
  --ink:#3b4450;
  --serif:"Cormorant Garamond", Georgia, serif;
  --sans:"Open Sans", Arial, sans-serif;
}
*{box-sizing:border-box;margin:0;padding:0}
html,body{width:1200px;height:542px;overflow:hidden;background:var(--bg)}
.canvas{position:relative;width:1200px;height:542px;font-family:var(--sans);color:var(--ink)}
.sheet{position:absolute;background:var(--paper);box-shadow:0 1px 4px rgba(0,0,0,.18);overflow:hidden}
.wave{position:absolute;left:0;bottom:0;width:100%}
.brand{display:flex;align-items:center;gap:6px}
.brand-dot{border-radius:50%;background:var(--blue);flex:none}
.brand-name{font-family:var(--serif);font-weight:600;color:var(--navy);letter-spacing:.06em;text-transform:uppercase;line-height:1.05;white-space:nowrap}
.brand-tag{font-size:5px;color:var(--grey);margin-top:2px;white-space:nowrap}
.web{position:absolute;left:0;width:100%;text-align:center;font-size:7px;letter-spacing:.18em;color:#fff}

/* letterhead */
.letterhead{left:19px;top:29px;width:336px;height:398px}
.letterhead .brand{position:absolute;left:18px;top:18px}
.letterhead .brand-dot{width:22px;height:22px}
.letterhead .brand-name{font-size:11px}
.watermark{position:absolute;left:103px;top:125px;width:130px;height:130px;border-radius:50%;background:var(--mist);opacity:.7}
.letterhead .web{bottom:10px}

/* folder */
.folder{left:372px;top:24px;width:348px;height:408px}
.folder .brand{position:absolute;left:0;right:0;top:120px;flex-direction:column;gap:8px}
.folder .brand-dot{width:38px;height:38px}
.folder .brand-name{font-size:17px}
.folder .brand-tag{font-size:6px}
.folder .web{bottom:30px;color:var(--blue);font-size:7px}

/* referral forms */
.form{top:29px;width:204px;height:398px;padding:10px}
.form-1{left:727px}.form-2{left:943px}
.form-frame{border:1.5px solid var(--blue);outline:1px solid var(--sky);outline-offset:-4px;height:100%;padding:12px 12px}
.form-head{text-align:center;border-bottom:1px solid var(--sky);padding-bottom:5px}
.form-head h2{font-family:var(--serif);font-weight:600;font-size:11px;color:var(--navy);letter-spacing:.05em}
.form-head p{font-size:4.5px;color:var(--ink);margin-top:2px}
.field{font-size:5px;display:flex;gap:3px;margin-top:10px}
.field span.line{flex:1;border-bottom:.6px solid var(--grey)}
.form h3{font-size:5.5px;font-weight:600;color:var(--blue);margin-top:10px}
.checks{display:grid;grid-template-columns:1fr 1fr;gap:3px 6px;margin-top:5px;list-style:none}
.checks li,.single li{font-size:4.5px;display:flex;align-items:center;gap:3px}
.checks li::before,.single li::before{content:"";width:5px;height:5px;border:.6px solid var(--ink);flex:none}
.single{list-style:none;display:grid;gap:3px;margin-top:5px}
.signature{font-size:5px;text-align:right;margin-top:14px;border-top:.6px solid var(--grey);padding-top:2px;margin-left:90px}

/* cards */
.card{width:115px;height:70px;top:449px}
.card-logo{left:19px}
.card-logo .brand{position:absolute;left:12px;top:16px}
.card-logo .brand-dot{width:14px;height:14px}
.card-logo .brand-name{font-size:8px}
.card-info{left:144px;padding:9px 10px}
.card-info .brand-name{font-size:6px}
.card-info p{font-size:4.5px;margin-top:3px;line-height:1.4}
.card-blue{background:linear-gradient(180deg,var(--blue),var(--navy));color:#fff;padding:10px}
.card-dr{left:955px}.card-team{left:1078px}
.card-blue h4{font-family:var(--serif);font-weight:600;font-size:8.5px;white-space:nowrap}
.card-blue p{font-size:4.5px;line-height:1.45;margin-top:3px;opacity:.92}
.card-team .brand-name{color:#fff;font-size:7px}
.card-team .brand-dot{width:11px;height:11px;background:#fff}

/* envelopes */
.envelope{top:444px;width:288px;height:86px}
.env-front{left:269px}
.env-front .brand{position:absolute;left:14px;top:12px}
.env-front .brand-dot{width:16px;height:16px}
.env-front .brand-name{font-size:8px}
.env-back{left:576px}
.env-back .web{bottom:8px;color:var(--blue);font-size:6px}
</style>
</head>
<body>
<div class="canvas">

  <!-- Letterhead -->
  <section class="sheet letterhead">
    <div class="brand">
      <span class="brand-dot"></span>
      <div><div class="brand-name">Corvale Dental Partners</div>
      <div class="brand-tag">Center for Endodontics, Periodontics and Implant Dentistry</div></div>
    </div>
    <div class="watermark"></div>
    <svg class="wave" viewBox="0 0 336 60" height="60" preserveAspectRatio="none">
      <defs><linearGradient id="lhWave" x1="0" x2="1"><stop offset="0" stop-color="#4f86cf"/><stop offset="1" stop-color="#0e2c5e"/></linearGradient></defs>
      <path d="M0 22 C90 6 200 40 336 14 L336 60 L0 60Z" fill="url(#lhWave)"/>
      <path d="M0 18 C90 2 200 36 336 10" fill="none" stroke="#9aa3ad" stroke-width="1.5"/>
    </svg>
    <div class="web">WWW.CORVALEDENTALPARTNERS.EXAMPLE</div>
  </section>

  <!-- Folder -->
  <section class="sheet folder">
    <div class="brand">
      <span class="brand-dot"></span>
      <div class="brand-name">Corvale Dental Partners</div>
      <div class="brand-tag">Center for Endodontics, Periodontics and Implant Dentistry</div>
    </div>
    <svg class="wave" viewBox="0 0 348 90" height="90" preserveAspectRatio="none" style="bottom:45px">
      <defs><linearGradient id="fdWave" x1="0" x2="1"><stop offset="0" stop-color="#0e2c5e"/><stop offset=".6" stop-color="#1f56a3"/><stop offset="1" stop-color="#4f86cf"/></linearGradient></defs>
      <path d="M0 40 C100 10 230 70 348 30 L348 62 C230 90 110 44 0 70Z" fill="url(#fdWave)"/>
      <path d="M0 34 C100 4 230 64 348 24" fill="none" stroke="#9aa3ad" stroke-width="1.5"/>
    </svg>
    <div class="web">WWW.CORVALEDENTALPARTNERS.EXAMPLE</div>
  </section>

  <!-- Periodontics referral form -->
  <section class="sheet form form-1">
    <div class="form-frame">
      <header class="form-head">
        <h2>Daniel Frayce, DDS</h2>
        <p>4820 Quillby Road NE, Suite 67, Harlow Falls, ND 58990</p>
        <p>Periodontics and Implant Dentistry</p>
      </header>
      <div class="field">Patient Name:<span class="line"></span>Date:<span class="line"></span></div>
      <h3>Evaluation of:</h3>
      <ul class="checks">
        <li>Periodontal evaluation</li><li>Implant consultation</li>
        <li>Crown lengthening</li><li>Gum grafting</li>
        <li>Extraction and graft</li><li>Sinus lift</li>
        <li>Ridge augmentation</li><li>Scaling and root planing</li>
        <li>Bone grafting</li><li>Frenectomy</li>
      </ul>
      <h3>Radiographs:</h3>
      <ul class="single"><li>Radiographs enclosed</li><li>FMX to be taken</li><li>Please take panoramic</li></ul>
      <h3>Referring Doctor:</h3>
      <div class="field">Name:<span class="line"></span></div>
      <div class="field">Phone:<span class="line"></span></div>
      <div class="field">Address:<span class="line"></span></div>
      <div class="signature">Signature</div>
    </div>
  </section>

  <!-- Endodontics referral form -->
  <section class="sheet form form-2">
    <div class="form-frame">
      <header class="form-head">
        <h2>Peter Ostrand, DDS</h2>
        <p>4820 Quillby Road NE, Suite 67, Harlow Falls, ND 58990</p>
        <p>Office Information</p>
      </header>
      <div class="field">Patient Name:<span class="line"></span>Date:<span class="line"></span></div>
      <h3>Evaluation of:</h3>
      <ul class="checks">
        <li>Root Canal Therapy</li><li>Root Canal Retreatment</li>
        <li>Apicoectomy</li><li>Other</li>
      </ul>
      <h3>Radiographs:</h3>
      <ul class="single"><li>Radiographs enclosed</li><li>FMX to be taken</li><li>Please take panoramic</li></ul>
      <h3>Referring Doctor:</h3>
      <div class="field">Name:<span class="line"></span></div>
      <div class="field">Phone:<span class="line"></span></div>
      <div class="field">Address:<span class="line"></span></div>
      <div class="signature">Signature</div>
    </div>
  </section>

  <!-- Business card: logo side -->
  <section class="sheet card card-logo">
    <div class="brand"><span class="brand-dot"></span><div class="brand-name">Corvale<br>Dental Partners</div></div>
    <svg class="wave" viewBox="0 0 115 20" height="20" preserveAspectRatio="none">
      <path d="M0 10 C35 2 75 18 115 6 L115 20 L0 20Z" fill="#1f56a3"/>
    </svg>
  </section>

  <!-- Business card: info side -->
  <section class="sheet card card-info">
    <div class="brand-name">Corvale Dental Partners</div>
    <p>Brenna K. Solvik, DDS<br>General and Cosmetic Dentistry</p>
    <p>4820 Quillby Road NE, Suite 67<br>Harlow Falls, ND 58990<br>info@corvaledentalpartners.example</p>
  </section>

  <!-- Envelope front -->
  <section class="sheet envelope env-front">
    <div class="brand">
      <span class="brand-dot"></span>
      <div><div class="brand-name">Corvale Dental Partners</div>
      <div class="brand-tag">4820 Quillby Road NE, Suite 67, Harlow Falls, ND 58990</div></div>
    </div>
    <svg class="wave" viewBox="0 0 288 22" height="22" preserveAspectRatio="none">
      <path d="M0 14 C90 4 190 22 288 8 L288 22 L0 22Z" fill="#1f56a3"/>
    </svg>
  </section>

  <!-- Envelope back -->
  <section class="sheet envelope env-back">
    <svg viewBox="0 0 288 86" width="288" height="86" style="position:absolute;left:0;top:0">
      <defs><linearGradient id="flap" x1="0" y1="0" x2="0" y2="1"><stop offset="0" stop-color="#0e2c5e"/><stop offset="1" stop-color="#4f86cf"/></linearGradient></defs>
      <path d="M0 0 L288 0 L160 56 Q144 62 128 56 Z" fill="url(#flap)"/>
    </svg>
    <div class="web">WWW.CORVALEDENTALPARTNERS.EXAMPLE</div>
  </section>

  <!-- Business card: doctor, blue -->
  <section class="sheet card card-blue card-dr">
    <h4>Peter Ostrand, DDS</h4>
    <p>Endodontics</p>
    <p>4820 Quillby Road NE, Suite 67<br>Harlow Falls, ND 58990<br>www.corvaledentalpartners.example</p>
  </section>

  <!-- Business card: team, blue -->
  <section class="sheet card card-blue card-team">
    <div class="brand"><span class="brand-dot"></span><div class="brand-name">Corvale<br>Dental Partners</div></div>
    <p>Brenna K. Solvik, DDS · Peter Ostrand, DDS<br>Daniel Frayce, DDS<br>info@corvaledentalpartners.example</p>
  </section>

</div>
</body>
</html>
```